Business Card Design Project

We need a logo design for a new company based in Southern California called "Norvale Security Services, Inc." We install security and camera systems for homeowners and business, to protect their assets.
Updates

Project Deadline Extended
Reason: LOGO Design completes in eight days. Would like that design decided before we finish the business cards. Thanks...

Target Market(s)

Homeowners and business owners looking for additional protection of their assets.

Industry/Entity Type

Security

Font styles to use
Serif

Requirements
Must have
• Company Name
Office# 555-472-3615
Service# 555-472-3616
email: NorvaleSecurity@brimwell.net
address: 48620 Thorncrest Lane Alder Springs, CA 90999
Nice to have
• Serving Southern California

```html
<!DOCTYPE html>
<html lang="en">
<head>
<meta charset="utf-8">
<title>Norvale Security Services, Inc. — Business Card</title>
<link rel="stylesheet" href="https://fonts.googleapis.com/css2?family=Merriweather:wght@400;700&display=swap">
<style>
  :root {
    --page-bg: #2b2622;
    --card-black: #0d0d0e;
    --card-edge: #1c1c1e;
    --brand-red: #e8202f;
    --label-red: #e33a43;
    --text-white: #f2f2f2;
  }
  * { margin: 0; padding: 0; box-sizing: border-box; }
  html, body {
    width: 1200px; height: 900px; overflow: hidden;
    background: var(--page-bg);
    font-family: "Merriweather", Georgia, serif;
  }
  .stage {
    width: 1200px; height: 900px;
    display: flex; align-items: center; justify-content: center;
  }
  .business-card {
    position: relative;
    width: 840px; height: 480px;
    background: var(--card-black);
    border: 1px solid var(--card-edge);
    border-radius: 18px;
    box-shadow: 0 24px 50px rgba(0,0,0,0.55);
    color: var(--text-white);
    overflow: hidden;
  }
  .brand-mark {
    position: absolute; left: 70px; top: 56px;
    display: flex; align-items: center; gap: 16px;
  }
  .brand-square { width: 30px; height: 30px; background: var(--brand-red); }
  .brand-name {
    font-size: 64px; font-weight: 700; letter-spacing: 2px;
    color: var(--brand-red); line-height: 1;
  }
  .company-name {
    position: absolute; left: 72px; top: 158px;
    font-size: 27px; font-weight: 400;
    font-variant: small-caps; letter-spacing: 4px;
    color: var(--text-white); white-space: nowrap;
  }
  .company-name .initial { color: var(--brand-red); }
  .address-band {
    position: absolute; left: 96px; top: 212px;
    width: 660px; height: 44px;
    background: var(--brand-red);
    display: flex; align-items: center; padding-left: 24px;
    font-size: 19px; font-weight: 700; color: var(--text-white);
    white-space: nowrap;
  }
  .contact-list {
    position: absolute; left: 120px; top: 298px; right: 40px;
    font-size: 20px; font-weight: 700;
  }
  .contact-row { display: flex; gap: 90px; margin-bottom: 40px; }
  .contact-item { white-space: nowrap; }
  .contact-label { color: var(--label-red); }
  .contact-value { color: var(--text-white); }
</style>
</head>
<body>
<main class="stage">
  <article class="business-card">
    <div class="brand-mark">
      <span class="brand-square"></span>
      <span class="brand-name">NORVALE</span>
    </div>
    <h1 class="company-name"><span class="initial">N</span>orvale <span class="initial">S</span>ecurity <span class="initial">S</span>ervices, Inc</h1>
    <p class="address-band">48620 Thorncrest Lane Alder Springs, CA 90999</p>
    <div class="contact-list">
      <div class="contact-row">
        <p class="contact-item"><span class="contact-label">Office</span> : <span class="contact-value">555-472-3615</span></p>
        <p class="contact-item"><span class="contact-label">Service</span> : <span class="contact-value">555-472-3616</span></p>
      </div>
      <div class="contact-row">
        <p class="contact-item"><span class="contact-label">E-mail</span> : <span class="contact-value">NorvaleSecurity@brimwell.net</span></p>
      </div>
    </div>
  </article>
</main>
</body>
</html>
```